The Velvet Leash Dog Walking Service Website Design

I am looking for a professional website that demonstrates our love of dogs and their need for socialization and exercise. It should inspire client trust with their furry family member by emphasizing our professionalism & warm hearts. The website should have a consistent look that represents our brand. It should include a landing page with video images rather than still images. The website will include service descriptions with an image for each service, prices, awards won, frequently asked questions, reviews, blog, and links to a feed for our socials and the software that we use for booking etc. The website will highlight the different locations that we service & provide an "about us" section for each location.

```html
<!DOCTYPE html>
<html lang="en">
<head>
<meta charset="utf-8">
<title>The Velvet Leash Dog Walking Service</title>
<link rel="stylesheet" href="https://fonts.googleapis.com/css2?family=Playfair+Display:ital,wght@0,400;0,600;0,700;1,700&family=Poppins:wght@400;500;600&display=swap">
<style>
:root{
  --teal:#3db4c7;
  --teal-dark:#2a95a8;
  --yellow:#f8e17a;
  --orange:#ef9a4f;
  --orange-dark:#e0823a;
  --purple:#6b3b70;
  --purple-dark:#55295a;
  --ink:#3d3d3d;
  --muted:#7a7a7a;
  --white:#ffffff;
  --paper:#f4f4f4;
}
*{box-sizing:border-box;margin:0;padding:0}
html,body{width:1200px;height:4576px;overflow:hidden}
body{font-family:"Poppins",Arial,sans-serif;color:var(--ink);background:var(--white);position:relative}
.abs{position:absolute}
.eyebrow{position:absolute;left:0;width:1200px;font-size:11px;letter-spacing:2px;text-transform:uppercase;color:var(--teal);font-weight:600;text-align:center}
.section-title{position:absolute;left:0;width:1200px;font-family:"Playfair Display",Georgia,serif;font-size:40px;color:var(--purple);text-align:center;font-weight:600;line-height:1.2}
.btn{display:inline-block;border-radius:20px;font-size:12px;font-weight:500;padding:9px 24px;text-decoration:none}
.btn-teal{background:var(--teal);color:var(--white)}
.btn-outline{border:1.5px solid var(--teal);color:var(--teal);background:var(--white)}
.center-row{position:absolute;left:0;width:1200px;display:flex;justify-content:center;gap:14px}

/* header */
.site-header{position:absolute;top:0;left:0;width:1200px;height:88px;background:rgba(255,255,255,.94);box-shadow:0 1px 6px rgba(0,0,0,.08)}
.brand-mark{position:absolute;left:206px;top:4px;width:104px;height:104px;border-radius:50%;background:var(--white);border:4px solid var(--teal);display:flex;align-items:center;justify-content:center;text-align:center;font-size:13px;font-weight:600;color:var(--purple);line-height:1.25;padding:12px}
.topbar{position:absolute;right:200px;top:12px;display:flex;align-items:center;gap:12px;font-size:12px;color:var(--ink)}
.topbar .dot{width:26px;height:26px;border-radius:50%;background:var(--orange)}
.main-nav{position:absolute;right:200px;top:58px;display:flex;gap:22px;font-size:12px}
.main-nav a{color:var(--ink);text-decoration:none;padding-bottom:4px}
.main-nav a.active{color:var(--teal);border-bottom:2px solid var(--teal)}

/* hero */
.hero-photo{position:absolute;top:0;left:0;width:1200px;height:560px;
  background:
   radial-gradient(ellipse 260px 320px at 560px 330px,rgba(92,86,96,.55),transparent 70%),
   radial-gradient(ellipse 230px 200px at 930px 420px,rgba(70,70,72,.55),transparent 70%),
   radial-gradient(ellipse 520px 260px at 180px 160px,rgba(84,110,66,.9),transparent 75%),
   radial-gradient(ellipse 420px 240px at 1050px 140px,rgba(98,116,74,.9),transparent 75%),
   linear-gradient(180deg,#c9d3b7 0%,#a8b486 35%,#cdb894 70%,#d8c6a3 100%)}
.hero-text{position:absolute;left:200px;top:280px;color:var(--white)}
.hero-text .kicker{font-size:12px;letter-spacing:2px;font-weight:600}
.hero-text h1{font-family:"Playfair Display",Georgia,serif;font-size:54px;font-weight:400;line-height:1.15;margin:4px 0 18px}
.hero-text h1 em{font-weight:700}

/* welcome */
.welcome{position:absolute;top:500px;left:0;width:1200px;height:466px;background:var(--yellow)}
.welcome-inner{position:absolute;left:220px;width:760px;top:650px;text-align:center}
.welcome-inner .eyebrow{position:static;width:auto}
.welcome-inner h2{font-family:"Playfair Display",Georgia,serif;font-size:36px;color:var(--purple);font-weight:600;margin-top:6px}
.welcome-inner p{font-size:11.5px;line-height:1.8;color:var(--ink);margin:16px 0 60px}

/* services */
.services-cards{position:absolute;top:1120px;left:200px;width:800px;display:flex;gap:16px}
.service-card{width:188px;height:360px;background:var(--white);box-shadow:0 2px 10px rgba(0,0,0,.12)}
.service-card .photo{height:132px}
.service-card h3{font-size:14px;font-weight:600;margin:14px 12px 8px;color:var(--ink);line-height:1.3}
.service-card p{font-size:10.5px;line-height:1.6;color:var(--muted);margin:0 12px}
.read-more{font-size:10.5px;color:var(--teal);font-weight:600;margin:10px 12px;display:block}

/* testimonials */
.reviews-band{position:absolute;top:1600px;left:0;width:1200px;height:540px;
  background:
   radial-gradient(ellipse 300px 200px at 950px 140px,rgba(255,210,160,.35),transparent 70%),
   radial-gradient(ellipse 300px 220px at 200px 380px,rgba(200,110,50,.35),transparent 70%),
   linear-gradient(180deg,#f0a25a 0%,var(--orange-dark) 100%)}
.review{position:absolute;top:1790px;width:360px;text-align:center;color:var(--white)}
.review .avatar{width:64px;height:64px;border-radius:50%;margin:0 auto 10px;border:3px solid var(--white)}
.stars{color:#ffd34d;font-size:14px;letter-spacing:2px}
.review p{font-size:11.5px;line-height:1.7;margin:10px 0}
.review .name{font-size:12px;font-weight:600}
.arrow{position:absolute;top:1930px;color:var(--white);font-size:26px}

/* articles */
.articles{position:absolute;top:2348px;left:200px;width:800px;display:flex;gap:20px}
.article-card{width:253px;height:370px;background:var(--white);box-shadow:0 2px 10px rgba(0,0,0,.12)}
.article-card .photo{height:200px}
.article-card .date{font-size:10.5px;color:var(--teal);margin:16px 14px 6px}
.article-card h3{font-size:14px;font-weight:600;line-height:1.35;margin:0 14px 8px}
.article-card p{font-size:10.5px;line-height:1.55;color:var(--muted);margin:0 14px}

/* awards */
.awards-band{position:absolute;top:2828px;left:0;width:1200px;height:380px;background:var(--purple)}
.award-badges{position:absolute;top:2985px;left:0;width:1200px;display:flex;justify-content:center;align-items:center;gap:22px}
.badge{background:var(--white);border:1px solid #ddd;display:flex;align-items:center;justify-content:center}
.badge-square{width:110px;height:100px}
.badge-square span{width:80px;height:70px;background:linear-gradient(180deg,#2f2f2f 0 45%,#c7c7c7 45% 100%)}
.badge-wide{width:150px;height:100px}
.badge-wide span{width:120px;height:52px;background:linear-gradient(180deg,#5a2b5f 0 60%,#b8a6bb 60% 100%);border-radius:2px}
.badge-round{width:110px;height:100px}
.badge-round span{width:74px;height:74px;border-radius:50%;background:radial-gradient(circle,#f3e9d9 0 45%,#b89aa6 46% 100%)}

/* areas */
.areas{position:absolute;top:3340px;left:200px;width:800px;display:flex;justify-content:space-between}
.area{width:180px;text-align:center}
.area .photo{width:160px;height:160px;border-radius:50%;border:5px solid var(--teal);margin:0 auto 16px}
.area .label{font-size:13px;font-weight:500;color:var(--purple)}

/* quote */
.quote-photo{position:absolute;top:3740px;left:0;width:1200px;height:440px;
  background:
   radial-gradient(ellipse 170px 200px at 830px 200px,rgba(112,78,60,.7),transparent 70%),
   radial-gradient(ellipse 200px 220px at 1040px 260px,rgba(60,60,64,.75),transparent 70%),
   radial-gradient(ellipse 140px 120px at 1040px 300px,rgba(235,235,235,.8),transparent 70%),
   linear-gradient(100deg,#f2f2f2 0%,#f2f2f2 44%,#c8c2ad 56%,#9aa486 80%,#7f8c6a 100%)}
.quote-box{position:absolute;top:3776px;left:200px;width:340px;height:340px;background:var(--teal);padding:26px 26px;color:var(--white);text-align:center}
.quote-box h2{font-family:"Playfair Display",Georgia,serif;font-size:30px;font-weight:600;line-height:1.2}
.quote-box .sub{font-size:12px;margin:2px 0 16px}
.field-row{display:flex;gap:10px;margin-bottom:8px}
.field{flex:1;height:30px;background:var(--white);border-radius:2px;font-size:10.5px;color:var(--muted);text-align:left;padding:8px 10px}
.field.tall{height:92px}
.send{background:var(--white);color:var(--teal);margin-top:8px;padding:7px 26px}

/* footer */
.site-footer{position:absolute;top:4180px;left:0;width:1200px;height:396px;background:var(--purple-dark)}
.footer-brand{position:absolute;left:200px;top:4240px;width:170px;height:170px;border-radius:50%;background:var(--white);border:5px solid var(--teal);display:flex;align-items:center;justify-content:center;text-align:center;font-size:15px;font-weight:600;color:var(--purple);padding:20px;line-height:1.3}
.footer-col{position:absolute;top:4236px;color:var(--white);font-size:11px;line-height:2}
.footer-col h4{font-size:14px;font-weight:600;margin-bottom:8px}
.socials{display:flex;gap:8px;margin-top:8px}
.socials span{width:24px;height:24px;border-radius:50%;background:var(--teal)}
.hours td{padding-right:22px}
.footer-bottom{position:absolute;top:4530px;left:200px;width:800px;display:flex;justify-content:space-between;font-size:10.5px;color:#d9c8dc}
.to-top{position:absolute;left:960px;top:4236px;color:var(--teal);font-size:22px;font-weight:600}
</style>
</head>
<body>

<!-- hero -->
<div class="hero-photo" role="img" aria-label="Woman walking a husky along a sunny tree-lined path"></div>
<div class="welcome"></div>
<svg class="abs" style="top:380px;left:0" width="1200" height="200" viewBox="0 0 1200 200" aria-hidden="true">
  <path d="M0,40 C260,170 520,190 760,120 C930,70 1080,40 1200,70 L1200,200 L0,200Z" fill="var(--yellow)"/>
  <path d="M0,40 C260,170 520,190 760,120 C930,70 1080,40 1200,70" fill="none" stroke="var(--teal)" stroke-width="5"/>
</svg>
<div class="hero-text">
  <div class="kicker">THE VELVET LEASH</div>
  <h1>Making <em>Tails</em> Wag</h1>
  <a class="btn btn-teal">Book Now</a>
</div>

<header class="site-header"></header>
<div class="brand-mark">The Velvet Leash</div>
<div class="topbar"><span>&#9742; (555) 014-2290</span><span class="dot"></span><a class="btn btn-outline" style="padding:5px 18px">Book Now</a></div>
<nav class="main-nav">
  <a class="active">Home</a><a>About Us</a><a>Services</a><a>Locations</a><a>Pricing</a><a>Reviews</a><a>Awards</a><a>FAQs</a><a>Blog</a><a>Contact Us</a>
</nav>

<!-- welcome -->
<div class="welcome-inner">
  <div class="eyebrow">Welcome To</div>
  <h2>Dog walker &amp; pet care provider</h2>
  <p>I have always been a caregiver. As a child, I spent every spare hour with the neighbourhood dogs, and that love has only grown. We started The Velvet Leash to give every pup daily exercise, friends to play with and a walker who truly cares. Our small team knows each dog by name, habit and favourite trail, so you can relax knowing your furry family member is safe, happy and well loved every single day.</p>
  <a class="btn btn-teal">Explore More</a>
</div>
<svg class="abs" style="top:950px;left:0" width="1200" height="30" viewBox="0 0 1200 30" aria-hidden="true">
  <path d="M280,16 L920,16" stroke="var(--teal)" stroke-width="3"/>
</svg>

<!-- services -->
<div class="eyebrow" style="top:1044px">What We Do</div>
<div class="section-title" style="top:1062px">Services we offer</div>
<div class="services-cards">
  <div class="service-card"><div class="photo" role="img" aria-label="Walker leading several dogs on a trail" style="background:linear-gradient(160deg,#a9b98a,#6f7f55 60%,#c8b58f)"></div><h3>Dog Walking</h3><p>Exercise, socialization and attention are vital for every dog. Our walks build confidence and burn energy in small, safe groups with a caring walker.</p><span class="read-more">Read More &rsaquo;</span></div>
  <div class="service-card"><div class="photo" role="img" aria-label="Dog resting at home" style="background:linear-gradient(160deg,#e7ddd0,#b79d80 60%,#7d6450)"></div><h3>House Calls</h3><p>Going away for the day? We drop by to feed, play and check in so your pet stays happy and relaxed at home.</p><span class="read-more">Read More &rsaquo;</span></div>
  <div class="service-card"><div class="photo" role="img" aria-label="Dog in a festive holiday setting" style="background:linear-gradient(160deg,#8c3b3b,#c98a5e 55%,#e9d3b0)"></div><h3>Holiday House Calls</h3><p>Holiday plans should not worry you. We keep routines steady with visits all season long.</p><span class="read-more">Read More &rsaquo;</span></div>
  <div class="service-card"><div class="photo" role="img" aria-label="Dog relaxing on a sofa" style="background:linear-gradient(160deg,#d8d2c8,#9c8f80 60%,#5e5650)"></div><h3>Dog Boarding in My Home</h3><p>A cozy home stay with walks, cuddles and a familiar face while you travel.</p><span class="read-more">Read More &rsaquo;</span></div>
</div>
<div class="center-row" style="top:1516px"><a class="btn btn-outline">Book Now</a><a class="btn btn-teal">Contact for Pricing</a></div>

<!-- testimonials -->
<div class="reviews-band" role="img" aria-label="Warm orange backdrop of a dog walk scene"></div>
<svg class="abs" style="top:1596px;left:0" width="1200" height="80" viewBox="0 0 1200 80" aria-hidden="true">
  <path d="M0,0 L1200,0 L1200,10 C800,70 400,70 0,10Z" fill="var(--white)"/>
</svg>
<div class="eyebrow" style="top:1676px;color:var(--white)">Reviews</div>
<div class="section-title" style="top:1694px;color:var(--white)">Happy clients say</div>
<span class="arrow" style="left:130px">&lsaquo;</span><span class="arrow" style="left:1058px">&rsaquo;</span>
<div class="review" style="left:220px"><div class="avatar" role="img" aria-label="Client's dog portrait" style="background:radial-gradient(circle at 50% 40%,#d9c3a0,#8a6b4e)"></div><div class="stars">&#9733;&#9733;&#9733;&#9733;&#9733;</div><p>&ldquo;Highly recommend! Our dog is always thrilled to see her walker. She comes home calm and happy, and the updates after each visit give us real peace of mind.&rdquo;</p><div class="name">Dana and Peter Holm</div></div>
<div class="review" style="left:620px"><div class="avatar" role="img" aria-label="Client's dog portrait" style="background:radial-gradient(circle at 50% 40%,#6d6a66,#2f2d2b)"></div><div class="stars">&#9733;&#9733;&#9733;&#9733;&#9733;</div><p>&ldquo;Caring, reliable and so kind. They learned every quirk of our shy rescue and helped him make new friends. We could not ask for better care.&rdquo;</p><div class="name">Maria Lindqvist</div></div>
<div class="center-row" style="top:2100px"><a class="btn btn-teal">View All</a></div>
<svg class="abs" style="top:2100px;left:0" width="1200" height="60" viewBox="0 0 1200 60" aria-hidden="true">
  <path d="M0,60 L0,45 C400,0 800,0 1200,45 L1200,60Z" fill="var(--white)"/>
  <path d="M0,45 C400,0 800,0 1200,45" fill="none" stroke="var(--teal)" stroke-width="4"/>
</svg>

<!-- articles -->
<div class="eyebrow" style="top:2276px">Latest Blog</div>
<div class="section-title" style="top:2294px">Recent Articles</div>
<div class="articles">
  <div class="article-card"><div class="photo" role="img" aria-label="Dog lying on the floor looking worried" style="background:linear-gradient(160deg,#efe6d8,#c7a77d 55%,#8a6a48)"></div><div class="date">August 18, 2023</div><h3>How to deal with separation anxiety in dogs</h3><p>Simple routines that help anxious dogs feel safe and calm when you leave.</p></div>
  <div class="article-card"><div class="photo" role="img" aria-label="Owner training a puppy outdoors" style="background:linear-gradient(160deg,#b4c59a,#7e8f5e 55%,#c14f52)"></div><div class="date">August 18, 2023</div><h3>Training methods for obedience in dogs</h3><p>Effective, gentle techniques for a well-mannered companion.</p></div>
  <div class="article-card"><div class="photo" role="img" aria-label="Dog playing in a park" style="background:linear-gradient(160deg,#a9c0cc,#6f8ea0 50%,#9a8a70)"></div><div class="date">August 18, 2023</div><h3>What is the best approach to training and socializing my dog?</h3><p>Training and socializing tips for a confident pup.</p></div>
</div>
<div class="center-row" style="top:2750px"><a class="btn btn-outline">View All</a></div>

<!-- awards -->
<div class="awards-band"></div>
<div class="eyebrow" style="top:2890px;color:var(--yellow)">The Velvet Leash</div>
<div class="section-title" style="top:2908px;color:var(--white)">Awards</div>
<svg class="abs" style="top:2960px;left:0" width="1200" height="250" viewBox="0 0 1200 250" aria-hidden="true">
  <path d="M250,250 C290,20 910,20 950,250Z" fill="var(--white)"/>
  <path d="M0,215 C400,160 800,160 1200,215 L1200,250 L0,250Z" fill="var(--white)"/>
  <path d="M0,215 C400,160 800,160 1200,215" fill="none" stroke="var(--teal)" stroke-width="4"/>
</svg>
<div class="award-badges">
  <div class="badge badge-square"><span></span></div>
  <div class="badge badge-wide"><span></span></div>
  <div class="badge badge-round"><span></span></div>
</div>

<!-- service areas -->
<div class="eyebrow" style="top:3256px">Locations</div>
<div class="section-title" style="top:3274px">Service Areas</div>
<div class="areas">
  <div class="area"><div class="photo" role="img" aria-label="Dog walker downtown" style="background:linear-gradient(160deg,#c8c4bc,#7c766e 60%,#4b4743)"></div><div class="label">Downtown Toronto</div></div>
  <div class="area"><div class="photo" role="img" aria-label="Dogs on the beach" style="background:linear-gradient(180deg,#b9d2de,#e4d8bf 60%,#c4ac86)"></div><div class="label">The Beaches</div></div>
  <div class="area"><div class="photo" role="img" aria-label="Dog walk on a leafy street" style="background:linear-gradient(160deg,#b4c493,#6e7f4f 60%,#c9b690)"></div><div class="label">Leslieville &amp; Riverdale</div></div>
  <div class="area"><div class="photo" role="img" aria-label="Dog in a city park" style="background:linear-gradient(160deg,#e0d3bd,#a98d6a 55%,#5f6a4a)"></div><div class="label">Yorkville</div></div>
</div>
<div class="center-row" style="top:3580px"><a class="btn btn-outline">View All</a></div>

<!-- quote -->
<div class="quote-photo" role="img" aria-label="Smiling woman hugging a husky outdoors"></div>
<div class="quote-box">
  <h2>Get Free Quote</h2>
  <div class="sub">Schedule Book Your Services Today!</div>
  <div class="field-row"><div class="field">First Name</div><div class="field">Phone</div></div>
  <div class="field-row"><div class="field">Email</div><div class="field">Subject</div></div>
  <div class="field-row"><div class="field tall">Type your Message...</div></div>
  <a class="btn send">Send</a>
</div>

<!-- footer -->
<div class="site-footer"></div>
<svg class="abs" style="top:4140px;left:0" width="1200" height="50" viewBox="0 0 1200 50" aria-hidden="true">
  <path d="M0,50 L0,40 C400,0 800,0 1200,40 L1200,50Z" fill="var(--purple-dark)"/>
</svg>
<div class="footer-brand">The Velvet Leash</div>
<div class="footer-col" style="left:420px">
  <h4>Contact Us</h4>
  <div>&#9742; (555) 014-2290</div>
  <div>&#9993; hello@velvetleash.com</div>
  <div>&#9906; 120 Maple Row,<br>Springfield, ON A1B 2C3</div>
  <div class="socials"><span></span><span></span><span></span></div>
</div>
<div class="footer-col" style="left:640px;line-height:1.75">
  <h4>Quick Links</h4>
  <div>Home</div><div>About Us</div><div>Services</div><div>Locations</div><div>Pricing</div><div>Reviews</div><div>Awards</div><div>FAQs</div><div>Blog</div><div>Contact Us</div>
</div>
<div class="footer-col" style="left:760px">
  <h4>Always Eager to Help</h4>
  <table class="hours" style="font-size:11px;color:var(--white);line-height:1.9">
    <tr><td>Mon</td><td>08:00 &ndash; 18:00</td></tr>
    <tr><td>Tue</td><td>08:00 &ndash; 18:00</td></tr>
    <tr><td>Wed</td><td>08:00 &ndash; 18:00</td></tr>
    <tr><td>Thu</td><td>08:00 &ndash; 18:00</td></tr>
    <tr><td>Fri</td><td>08:00 &ndash; 18:00</td></tr>
    <tr><td>Sat</td><td>09:00 &ndash; 15:00</td></tr>
    <tr><td>Sun</td><td>Closed</td></tr>
  </table>
  <a class="btn btn-teal" style="margin-top:12px">Book Now</a>
</div>
<div class="to-top">&#8593;</div>
<div class="footer-bottom"><span>&copy; 2023 The Velvet Leash. All Rights Reserved.</span><span>Privacy Policy &nbsp;|&nbsp; Terms &amp; Conditions</span></div>

</body>
</html>
```